Stationary (letterhead, envelopes, business cards and e-mail signature) for law firm
Law Office of Warren T. Felding
Creative Brief
Professional
Warren T. Felding
Attorney at Law
41 Linden Court, Suite 500 Irvine, California 92731
wfelding@lawwtf-example.com
www.lawwtf-example.com
I would also like my direct dial phone number to appear on the card (in addition to my main number. The Direct number is (714) 555-0187
I would like my logo and maybe my website address to appear on the back. Please be creative.

```html
<!DOCTYPE html>
<html lang="en">
<head>
<meta charset="utf-8">
<title>Law Office of Warren T. Felding — Stationery</title>
<link href="https://fonts.googleapis.com/css2?family=Cinzel:wght@400;500&display=swap" rel="stylesheet">
<style>
  :root{
    --board:#d6d6d6;
    --paper:#ffffff;
    --navy:#17204a;
    --slate:#8c8c8c;
    --ink:#2a2f4a;
    --faint:#e3e5ee;
    --soft-edge:#c4c4c4;
  }
  *{box-sizing:border-box;margin:0;padding:0}
  html,body{width:1200px;height:754px;overflow:hidden}
  body{background:var(--board);font-family:"Cinzel",serif;color:var(--ink);position:relative}
  .piece{position:absolute;background:var(--paper);overflow:hidden;box-shadow:0 1px 3px rgba(0,0,0,.18)}
  .card{border-radius:10px}

  .brand{display:flex;align-items:center;gap:8px}
  .brand-mark{width:14px;height:14px;background:var(--navy);flex:none}
  .brand-text{line-height:1.05;color:var(--ink)}
  .brand-kicker{font-size:8px;letter-spacing:2px;color:#7d8196}
  .brand-name{font-size:14px;letter-spacing:1px}

  .watermark{position:absolute;color:var(--faint);font-weight:400;letter-spacing:-2px;line-height:1;white-space:nowrap}

  /* Letterhead */
  .letterhead{left:48px;top:48px;width:492px;height:665px}
  .letterhead .brand{position:absolute;left:24px;top:26px}
  .letterhead .watermark{right:8px;bottom:14px;font-size:112px}
  .letterhead-footer{position:absolute;left:24px;bottom:24px;font-size:8.5px;line-height:1.45;letter-spacing:.4px}

  /* Business cards */
  .card-front{left:569px;top:48px;width:204px;height:125px}
  .card-front .brand{position:absolute;left:14px;top:16px}
  .card-front .brand-mark{width:9px;height:9px}
  .card-front .brand-kicker{font-size:5px;letter-spacing:1px}
  .card-front .brand-name{font-size:9px}
  .card-front .title{position:absolute;left:96px;top:44px;font-size:5.5px;letter-spacing:.6px;color:#7d8196}
  .card-front .contact{position:absolute;left:96px;top:58px;font-size:5.5px;line-height:1.45;letter-spacing:.3px}

  .card-back{display:flex;flex-direction:column;align-items:center;justify-content:center;gap:14px}
  .card-back .mono{font-size:22px;letter-spacing:1px}
  .card-back .url{font-size:6px;letter-spacing:.8px}
  .card-back-white{left:874px;top:113px;width:208px;height:117px}
  .card-back-navy{left:658px;top:206px;width:206px;height:116px;background:var(--navy);color:var(--paper)}
  .card-back-slate{left:893px;top:259px;width:209px;height:113px;background:var(--slate);color:var(--paper)}

  /* Envelope */
  .envelope{left:569px;top:384px;width:559px;height:329px;border-radius:4px}
  .envelope-flap{position:absolute;left:0;top:0;width:559px;height:92px}
  .flap-name{position:absolute;left:0;right:0;top:22px;text-align:center;color:var(--paper);font-size:20px;letter-spacing:2px}
  .envelope .brand{position:absolute;left:14px;top:112px}
  .envelope .return{position:absolute;left:14px;top:150px;font-size:7.5px;line-height:1.5;letter-spacing:.4px}
  .envelope .watermark{right:8px;bottom:4px;font-size:96px}
</style>
</head>
<body>

  <section class="piece letterhead" aria-label="Letterhead">
    <div class="brand">
      <span class="brand-mark"></span>
      <div class="brand-text">
        <div class="brand-kicker">LAW OFFICE OF</div>
        <div class="brand-name">WARREN T. FELDING</div>
      </div>
    </div>
    <div class="watermark">Felding</div>
    <address class="letterhead-footer" style="font-style:normal">
      41 Linden Court, Suite 500 &nbsp;Irvine, California 92731<br>
      Phone (714) 555-0110 &nbsp;|&nbsp; Fax (714) 555-0142<br>
      Email wfelding@lawwtf-example.com &nbsp;|&nbsp; www.lawwtf-example.com
    </address>
  </section>

  <section class="piece card card-front" aria-label="Business card front">
    <div class="brand">
      <span class="brand-mark"></span>
      <div class="brand-text">
        <div class="brand-kicker">LAW OFFICE OF</div>
        <div class="brand-name">WARREN T. FELDING</div>
      </div>
    </div>
    <div class="title">Attorney at Law</div>
    <address class="contact" style="font-style:normal">
      41 Linden Court, Suite 500<br>
      Irvine, California 92731<br>
      Main (714) 555-0110<br>
      Direct (714) 555-0187<br>
      wfelding@lawwtf-example.com
    </address>
  </section>

  <section class="piece card card-back card-back-white" aria-label="Business card back, white">
    <div class="mono">Felding</div>
    <div class="url">www.lawwtf-example.com</div>
  </section>

  <section class="piece card card-back card-back-navy" aria-label="Business card back, navy">
    <div class="mono">Felding</div>
    <div class="url">www.lawwtf-example.com</div>
  </section>

  <section class="piece card card-back card-back-slate" aria-label="Business card back, grey">
    <div class="mono">Felding</div>
    <div class="url">www.lawwtf-example.com</div>
  </section>

  <section class="piece envelope" aria-label="Envelope">
    <svg class="envelope-flap" viewBox="0 0 559 92" preserveAspectRatio="none" aria-hidden="true">
      <path d="M0 0 H559 V62 Q559 70 548 70 H310 L279.5 92 L249 70 H11 Q0 70 0 62 Z" fill="var(--navy)"/>
    </svg>
    <div class="flap-name">Felding</div>
    <div class="brand">
      <span class="brand-mark"></span>
      <div class="brand-text">
        <div class="brand-kicker">LAW OFFICE OF</div>
        <div class="brand-name">WARREN T. FELDING</div>
      </div>
    </div>
    <address class="return" style="font-style:normal">
      41 Linden Court, Suite 500<br>
      Irvine, California 92731
    </address>
    <div class="watermark">Felding</div>
  </section>

</body>
</html>
```